Alcohol designs Birthday Sign's needs more templates

We are after 10 new designs for signable custom birthday signs, alcohol theme inspired (beer, wine, spirits) for this batch, You do not need to provide 10 designs however the winner will be based on final look and quantity.
For example someone may win with one design or ten designs. We will also look at purchasing more individual designs for any winners or potential winners. Designs must be in layers, CMYK, 8bits channel, saved as TIFF or PDS or AI, size is 460mm wide x by 1060mm high with 30mm bleed included, total graphic size will be 430 x 1030 at 300ppi, any text must be editable and font files included. see attached for sample's, signable area needs to be on each design and a sample persons name, other then that we a excited to see what everyone comes up with
Updates
Reason: Allow more designs to be supplied form current designers and new designers. Also to allow us to choose more than one designer by adding a second/third place
Target Market(s)
Birthday
Requirements
Must have
- Layers.
- Space for people to sign
Nice to have
- At least 3 designs (These can be of the same template you design just with a small them change beer, wine etc)

```html
<!DOCTYPE html>
<html lang="en">
<head>
<meta charset="utf-8">
<title>Keep Calm and Drink Beer – 21st Birthday Sign</title>
<link href="https://fonts.googleapis.com/css2?family=Orbitron:wght@400;500;700;900&family=Exo+2:wght@400;500&display=swap" rel="stylesheet">
<style>
  :root {
    --paper: #ffffff;
    --amber-light: #ffdc78;
    --amber: #fdc14e;
    --amber-deep: #f7a92b;
    --malt-brown: #5b2a0b;
  }
  html, body {
    margin: 0;
    padding: 0;
    width: 1200px;
    height: 2761px;
    overflow: hidden;
    background: var(--paper);
  }
  .sign {
    position: relative;
    width: 1200px;
    height: 2761px;
    overflow: hidden;
    background: var(--paper);
  }
  .sign__panel {
    position: absolute;
    left: 40px;
    top: 40px;
    width: 1118px;
    height: 2674px;
    background: radial-gradient(ellipse 70% 45% at 50% 45%, var(--amber-light) 0%, var(--amber) 60%, var(--amber-deep) 100%);
  }
  .beer-illustration {
    position: absolute;
    left: 65px;
    top: 185px;
    width: 1070px;
    height: 630px;
    border-radius: 46% 46% 30% 30%;
    background: radial-gradient(ellipse at 50% 45%, #fff4d6 0%, #f9b02e 45%, #6b3210 100%);
    opacity: 0.9;
  }
  .headline {
    position: absolute;
    left: 0;
    width: 1200px;
    margin: 0;
    text-align: center;
    font-family: "Orbitron", sans-serif;
    font-weight: 900;
    font-size: 120px;
    line-height: 1;
    letter-spacing: 4px;
    color: var(--malt-brown);
  }
  .headline--top { top: 885px; }
  .headline--bottom { top: 1162px; }
  .connector {
    position: absolute;
    top: 1055px;
    left: 0;
    width: 1200px;
    display: flex;
    align-items: center;
    justify-content: center;
    gap: 44px;
  }
  .connector__word {
    font-family: "Orbitron", sans-serif;
    font-weight: 900;
    font-size: 78px;
    line-height: 1;
    letter-spacing: 3px;
    color: var(--malt-brown);
  }
  .double-rule {
    display: block;
    height: 16px;
    border-top: 5px solid var(--malt-brown);
    border-bottom: 5px solid var(--malt-brown);
    box-sizing: border-box;
  }
  .connector .double-rule { width: 166px; }
  .signing-area {
    position: absolute;
    left: 80px;
    top: 1330px;
    width: 1040px;
    height: 880px;
  }
  .celebrant {
    position: absolute;
    left: 0;
    top: 2270px;
    width: 1200px;
    height: 360px;
  }
  .celebrant__swash {
    position: absolute;
    top: 30px;
    width: 300px;
    height: 46px;
    border-radius: 23px;
    background: var(--malt-brown);
  }
  .celebrant__swash--left { left: 166px; }
  .celebrant__swash--right { right: 166px; }
  .celebrant__age {
    position: absolute;
    top: 20px;
    left: 0;
    width: 1200px;
    text-align: center;
    font-family: "Exo 2", sans-serif;
    font-weight: 400;
    font-size: 64px;
    line-height: 1;
    color: var(--malt-brown);
  }
  .celebrant__age sup {
    font-size: 36px;
    vertical-align: 26px;
  }
  .celebrant__name {
    position: absolute;
    top: 108px;
    left: 0;
    width: 1200px;
    margin: 0;
    text-align: center;
    font-family: "Orbitron", sans-serif;
    font-weight: 900;
    font-size: 140px;
    line-height: 1;
    letter-spacing: 6px;
    color: var(--malt-brown);
  }
  .celebrant__occasion {
    position: absolute;
    top: 262px;
    left: 0;
    width: 1200px;
    display: flex;
    align-items: center;
    justify-content: center;
    gap: 14px;
  }
  .celebrant__occasion .double-rule { width: 236px; }
  .celebrant__occasion-word {
    font-family: "Exo 2", sans-serif;
    font-weight: 500;
    font-size: 66px;
    line-height: 1;
    letter-spacing: 3px;
    color: var(--malt-brown);
  }
</style>
</head>
<body>
<main class="sign">
  <div class="sign__panel"></div>

  <div class="beer-illustration" role="img" aria-label="Illustration of two foaming beer mugs clinking together, framed by wheat ears and floating bubbles"></div>

  <h1 class="headline headline--top">KEEP CALM</h1>
  <div class="connector">
    <span class="double-rule"></span>
    <span class="connector__word">AND</span>
    <span class="double-rule"></span>
  </div>
  <p class="headline headline--bottom">DRINK BEER</p>

  <div class="signing-area" aria-label="Space for guests to sign"></div>

  <section class="celebrant">
    <div class="celebrant__swash celebrant__swash--left" role="img" aria-label="Decorative swash ornament"></div>
    <div class="celebrant__swash celebrant__swash--right" role="img" aria-label="Decorative swash ornament"></div>
    <div class="celebrant__age">It's 21<sup>st</sup></div>
    <h2 class="celebrant__name">MASON</h2>
    <div class="celebrant__occasion">
      <span class="double-rule"></span>
      <span class="celebrant__occasion-word">Birthday</span>
      <span class="double-rule"></span>
    </div>
  </section>
</main>
</body>
</html>
```